Dynamic Website Design For Dynamic Speaker and Business Coach!

Professional Website Design for a for a Professional Business coach, Business trainer, and Speaker.

Note: This is for design only. No coding required. We want to see your ideas for a great website! This will be a FUN design and not boring like others you may work on.

Please let your creative ideas flow. We have given you a ton of info along with videos to help you understand what we are after, however we WANT your creativity to shine through in your designs!

We are a professional company that has run hundreds of crowdsourced projects on multiple platforms. If you participate in this contest (we hope you do) you can expect great video feedback, consistent feedback, and also our guarantee that if we know your website design will not be what we are looking for we will notify you so you don’t waste your time if there is no chance of you winning.

We respect and recognize this is how you make your living and we will not play games. We look forward to an awesome contest and awesome website designs.

Design Brief:

We are looking for a fresh and fun new design for

http://www.brightpath-advisory.net

This individual (Dana Holloway) teaches and trains corporations and businesses in the fields of leadership, sales, communication, business operations etc. Additionally this business teaches and mentors business professionals in a small group level or 1 on 1.

The website needs to convey trust, professionalism, and affluent, while at the same time having some personality!

This business operates on 3 core principles that we would like to see incorporated into the logo if it is a good fit. The 3 principals are:

Focus
Accountability
Results

Here is a video to help explain what we like about the current site and what we don’t like:
http://clipvault.example/t/QwpLmr82kTnb

As you can see the website is geared towards business professionals. Please look over the website to learn what they do. Obviously this is not a good website so we need your help.

We want a website that is professional-looking, has personality and is geared more towards promoting Dana Holloway, the owner of Summit Path Advisory as a Speaker and Business Consultant. The more you can incorporate clean, professional and fun personality elements into the design, the better off you are at winning.

Here are some examples of other sites in their business that have some things we like:

http://velvetcompass.com Please watch video to learn what we like and don’t like:
http://clipvault.example/t/NrtHq7YpLwc

http://tallpinegrowth.com Please watch video to learn what we like and don’t like:
http://clipvault.example/t/J8vDkrWa

http://www.marthaquince.com Please watch video to learn what we like and don’t like:
http://clipvault.example/t/Pz3mx9Rb2Kq

http://www.vantix7.com Please watch video to learn what we like and don’t like:
http://clipvault.example/t/7Gwe4sNhydv

NOTE: We do not want to copy anything outright. We want to learn, model and take their ideas and make them better. We also want to be flexible and take what we like along with your creativity to make an amazing design.

Here is what we are looking for in more specific terms:

Colors: We like the darker blue (not the light blue like the site) and also a burnt orange. I’ve attached her Logo so you can get an idea and feel for the colors.

When looking at colors please know that the current site and look is NOT what we are going for. We are going for a clean and professional look but also a look that is BOLD, FUN, and Vibrant (hence the colors).

Menu: Horizontal. We like bold and easy to read menu items. Don’t make it small and cluttered.

Site Structure: Clean and easy to navigate. We have a lot of content to display so we need a clean structure that breaks up the text and content areas.
Images: Please pull images from the current site. We can always replace the images of course, but if you show them “their own stuff” in the new design you will be closer to winning because it will feel more like “them”

Look and Feel: Professional. Fun. High-End. Business-like. This website needs to convey that Dana Holloway and Summit Path Advisory are professional. That Dana Holloway is a sought-after Speaker and Business Consultant who knows what she is talking about; can be serious when she needs to be, but also likes to have fun with her clients. This site must convey that!

Content Areas: It is a safe bet that if it is on the current site we need it on the new site. So don’t drop anything as it makes it hard to “cut content”.

What we don't want: We do not want clutter, boring, or templates or themes. We don’t want too cartoony, too cute, or too fancy… Be creative!

Out of respect to professional designers who really are working hard to win if you do not follow this brief, you submit worn out themes, templates, or boring designs you will be eliminated. We are offering great prize money for this so we expect great visual designs.
Updates

Project Deadline Extended
Reason: Our client is out of town, and waiting to hear feedback from them. So, in the meantime, we wanted to keep the project going to see what else you designers can come up with. As soon as we hear back from our client, we will pass along the info. Thanks!

Target Market(s)

Target Audience is entrepreneurs and business professionals alike. This is all business to business stuff.

This person teaches and trains startups and billion dollar companies. The common thread is that they are all businesses and companies who need help in various areas including sales, communication, business operations, etc.

Industry/Entity Type

Business

Font styles to use
Sans Serif

Requirements
Must have
• Brief is very detailed. Please review
Nice to have
Should not have

```html
<!DOCTYPE html>
<html lang="en">
<head>
<meta charset="utf-8">
<title>Summit Path Advisory</title>
<link href="https://fonts.googleapis.com/css2?family=Bree+Serif&family=Lato:wght@400;700&family=Open+Sans:ital,wght@0,400;0,600;1,400&family=Roboto:wght@400;500&display=swap" rel="stylesheet">
<style>
:root{
  --blue:#27348b;
  --nav-top:#2f5184;
  --nav-bottom:#1c3461;
  --orange:#e38b25;
  --orange-btn:#f07a22;
  --text:#5a5a5a;
  --muted:#8c8c8c;
  --panel:#efefeb;
  --footer:#ebebe7;
  --line:#dcdcdc;
  --white:#fff;
}
*{box-sizing:border-box;margin:0;padding:0}
html,body{width:882px;height:1200px;overflow:hidden;background:var(--white)}
body{position:relative;font-family:"Open Sans",Arial,sans-serif;color:var(--text)}
.abs{position:absolute}

/* header */
.brand{left:78px;top:18px;display:flex;align-items:center;gap:10px}
.brand-dot{width:40px;height:40px;border-radius:50%;background:var(--orange)}
.brand-name{font-family:"Lato",sans-serif;font-weight:700;font-size:26px;color:var(--blue);line-height:1}
.phone{left:662px;top:15px;display:flex;align-items:center;gap:8px;font-family:"Lato",sans-serif;font-size:17px;color:var(--blue)}
.search{left:660px;top:47px;width:143px;height:25px;display:flex}
.search-field{flex:1;border:1px solid #ddd;border-right:none;font-size:10px;color:#999;padding:5px 8px}
.search-btn{width:27px;background:var(--orange-btn);display:flex;align-items:center;justify-content:center}

/* navigation */
.nav{left:0;top:80px;width:882px;height:36px;background:linear-gradient(var(--nav-top),var(--nav-bottom))}
.nav ul{list-style:none;display:flex;position:absolute;left:78px;top:0;height:36px}
.nav li{font-family:"Lato",sans-serif;font-weight:700;font-size:12.5px;color:var(--white);padding:0 8px;line-height:36px}
.nav li.active{background:var(--orange);padding:0 9px 0 12px}

/* hero */
.hero{left:0;top:116px;width:882px;height:287px;background:var(--orange)}
.hero-video{left:79px;top:165px;width:306px;height:198px;border:1px solid #f2c28a;background:linear-gradient(135deg,#d0732b,#b35a22 60%,#c96a2a)}
.video-bar{position:absolute;left:0;bottom:0;width:100%;height:24px;background:#111;border-top:1px solid #333}
.hero-title{left:520px;top:155px;width:260px;text-align:center;font-family:"Bree Serif",serif;font-size:31px;line-height:41px;color:var(--white)}
.cta{left:566px;top:330px;width:164px;height:38px;background:linear-gradient(#f68a2e,#e6651a);border-radius:3px;color:var(--white);font-family:"Roboto",sans-serif;font-weight:500;font-size:17px;text-align:center;line-height:38px;box-shadow:0 6px 8px rgba(0,0,0,.18)}

/* survey popup */
.survey{left:443px;top:364px;width:177px;height:193px;background:var(--white);border:1px solid #bbb;font-family:"Roboto",sans-serif}
.survey-q{position:absolute;left:10px;top:10px;width:157px;text-align:center;font-weight:500;font-size:11.5px;line-height:18px;color:#111}
.survey-opt{position:absolute;left:10px;width:154px;background:#9a9a9a;border:1px solid #555;border-radius:4px;font-size:11px;color:#222;padding:6px 8px 6px 27px}
.survey-opt::before{content:"";position:absolute;left:8px;top:7px;width:11px;height:11px;border-radius:50%;background:var(--white);border:1px solid #777}
.survey-close{left:598px;top:357px}

/* services */
.service-panel{left:328px;top:431px;width:226px;height:205px;background:var(--panel);border-bottom:5px solid #d8d8d4}
.service{top:448px;width:250px;text-align:center}
.service-icon{width:72px;height:72px;border-radius:50%;background:#ececea;margin:0 auto;display:flex;align-items:center;justify-content:center}
.service-icon.accent{background:var(--orange)}
.service h3{font-family:"Lato",sans-serif;font-weight:400;font-size:17px;color:var(--blue);margin-top:10px}
.service p{font-size:11.5px;line-height:15px;color:var(--text);margin-top:2px}
.more{display:inline-block;margin-top:9px;width:60px;height:23px;background:var(--blue);color:var(--white);font-family:"Lato",sans-serif;font-size:13px;line-height:23px;box-shadow:0 2px 3px rgba(0,0,0,.25)}

/* section headings */
.sec-title{display:flex;align-items:center;gap:10px;font-family:"Lato",sans-serif;font-weight:700;font-size:16px;color:var(--blue)}
.sec-mark{width:24px;height:24px;border-radius:50%;background:var(--orange)}
.dotted{height:0;border-top:1px dotted #cfcfcf}
.arrows{font-size:12px;color:#666;letter-spacing:3px}
.arrows.blue{color:var(--blue);font-weight:700}

.photo{background:linear-gradient(#5a4438,#8aa6b8);border:4px solid var(--white);outline:1px solid #ddd}
.welcome-text{left:185px;top:710px;width:366px;font-size:12px;line-height:16.8px;color:var(--text)}
.read-more{left:482px;top:835px;font-size:10px;color:var(--orange)}
.vdivider{width:0;border-left:1px solid #e6e6e6}

.side-video{left:593px;top:712px;width:210px;height:135px;background:linear-gradient(135deg,#c9702c,#a85524);box-shadow:0 6px 8px rgba(0,0,0,.25)}
.side-video .video-bar{height:12px}

.band{left:0;top:878px;width:882px;height:12px;background:linear-gradient(#f1f1f1,#fff)}

.quote{left:80px;top:940px;width:380px;font-size:11.5px;line-height:16.2px;color:var(--text);letter-spacing:.2px}
.qmark{font-family:"Bree Serif",serif;color:var(--blue);font-size:18px;line-height:0}
.quote-name{left:81px;top:1009px;font-style:italic;font-size:10px;color:#333}
.quote-photo{left:473px;top:943px;width:76px;height:79px;border:2px solid var(--blue);border-radius:3px;background:linear-gradient(#d9c2a8,#7f8d9c)}

.members{left:593px;top:942px;width:211px;height:80px;border:2px solid var(--blue);border-radius:4px;display:flex;align-items:center;justify-content:space-around}
.badge{width:50px;height:50px;border-radius:50%;background:#2c4f8a}
.badge.sq{border-radius:0;width:42px;height:44px;background:linear-gradient(#d8453a,#3b74b8)}
.badge.gold{background:#c9a43a}

/* footer */
.footer{left:0;top:1055px;width:882px;height:107px;background:var(--footer);border-top:1px solid #ddd}
.foot-mark{left:79px;top:1086px;width:64px;height:58px;border-radius:50%;background:#7d7d7d}
.foot-links{left:169px;top:1074px;font-size:10.5px;color:var(--muted)}
.foot-links span{color:#b5b5b5;margin:0 3px}
.share{left:170px;top:1123px;font-size:11.5px;color:var(--muted);display:flex;align-items:center;gap:10px}
.soc{width:26px;height:26px;border-radius:50%;box-shadow:0 1px 2px rgba(0,0,0,.3)}
.subscribe{right:80px;top:1102px;font-size:12px;color:var(--muted)}
.subscribe b{color:#777}
.email{left:512px;top:1125px;width:230px;height:25px;background:var(--white);font-style:italic;font-size:9.5px;color:#555;padding:6px 8px}
.submit{left:743px;top:1124px;width:60px;height:26px;background:var(--orange-btn);color:var(--white);font-family:"Lato",sans-serif;font-weight:700;font-size:12px;text-align:center;line-height:26px;border-radius:2px}
.bottom{left:0;top:1162px;width:882px;height:38px;background:var(--blue);font-size:10px;color:#e0e3f0}
</style>
</head>
<body>

<header>
  <div class="abs brand"><span class="brand-dot"></span><span class="brand-name">Summit Path Advisory</span></div>
  <div class="abs phone">
    <svg width="18" height="14" viewBox="0 0 18 14"><path d="M1 4c4-4 12-4 16 0l-2 2-3-1V3C10 2 8 2 6 3v2L3 6z" fill="#27348b"/><rect x="4" y="7" width="10" height="7" rx="1" fill="#27348b"/></svg>
    (555) 418-2760
  </div>
  <div class="abs search">
    <div class="search-field">Search....</div>
    <div class="search-btn"><svg width="14" height="14" viewBox="0 0 14 14"><circle cx="8" cy="6" r="4" fill="none" stroke="#fff" stroke-width="1.6"/><line x1="5" y1="9" x2="1.5" y2="12.5" stroke="#fff" stroke-width="1.8"/></svg></div>
  </div>
</header>

<nav class="abs nav">
  <ul>
    <li class="active">Home</li><li>Passion</li><li>Who We Are</li><li>Speaker</li><li>Free Videos</li><li>Web TV Show</li><li>Testimonials</li><li>Oakridge Learning</li><li>Blog</li><li>Contact Us</li>
  </ul>
</nav>

<section class="abs hero"></section>
<div class="abs hero-video" role="img" aria-label="Video still of the coach speaking in front of an orange backdrop">
  <div class="video-bar">
    <svg width="304" height="24" viewBox="0 0 304 24"><path d="M10 7l7 5-7 5z" fill="#fff"/><path d="M30 10h3l4-3v10l-4-3h-3z" fill="#ccc"/><rect x="48" y="10" width="220" height="4" rx="2" fill="#444"/><rect x="48" y="10" width="64" height="4" rx="2" fill="#d21f1f"/><path d="M284 8h4M288 8v4M284 16l-2 0M282 16v-4" stroke="#fff" stroke-width="1.5"/></svg>
  </div>
</div>
<h1 class="abs hero-title">Do You Need More Focus Accountability &amp; Results?</h1>
<div class="abs cta">FIND OUT NOW</div>

<section class="abs service-panel"></section>
<div class="abs service" style="left:61px">
  <div class="service-icon"><svg width="34" height="34" viewBox="0 0 34 34"><path d="M17 3a11 11 0 0 0-11 11c0 4 2 6 3 8v9h11v-4h4a2 2 0 0 0 2-2v-4l3-1-3-5A11 11 0 0 0 17 3z" fill="#e6782a"/><circle cx="15" cy="13" r="3" fill="#fff"/></svg></div>
  <h3>Professional Business Coach</h3>
  <p>Lorem ipsum dolor sit amet, ewrewr eri<br>consectetuer adipiscing elit erwerwer.</p>
  <span class="more">More</span>
</div>
<div class="abs service" style="left:316px">
  <div class="service-icon accent"><svg width="34" height="34" viewBox="0 0 34 34"><rect x="5" y="6" width="24" height="18" rx="2" fill="none" stroke="#fff" stroke-width="2.5"/><line x1="17" y1="24" x2="17" y2="30" stroke="#fff" stroke-width="2.5"/></svg></div>
  <h3>Business Trainer</h3>
  <p>Lorem ipsum dolor sit amet, ewrewr eri<br>consectetuer adipiscing elit erwerwer.</p>
  <span class="more">More</span>
</div>
<div class="abs service" style="left:573px">
  <div class="service-icon"><svg width="38" height="34" viewBox="0 0 38 34"><circle cx="16" cy="12" r="4" fill="#e6782a"/><path d="M9 22c0-4 3-6 7-6s7 2 7 6z" fill="#e6782a"/><rect x="5" y="22" width="22" height="3" fill="#e6782a"/><rect x="12" y="25" width="8" height="6" fill="#e6782a"/><ellipse cx="29" cy="6" rx="6" ry="4" fill="#e6782a"/></svg></div>
  <h3>Business Speaker</h3>
  <p>Lorem ipsum dolor sit amet, ewrewr eri<br>consectetuer adipiscing elit erwerwer.</p>
  <span class="more">More</span>
</div>

<aside class="abs survey">
  <p class="survey-q">Does your business have paying customers?</p>
  <div class="survey-opt" style="top:57px;height:25px">Yes.</div>
  <div class="survey-opt" style="top:90px;height:25px">No.</div>
  <div class="survey-opt" style="top:128px;height:48px">Not yet, but it will Soon!</div>
</aside>
<svg class="abs survey-close" width="26" height="26" viewBox="0 0 26 26"><circle cx="13" cy="13" r="11.5" fill="#fff" stroke="#111" stroke-width="2.5"/><path d="M8.5 8.5l9 9M17.5 8.5l-9 9" stroke="#111" stroke-width="3"/></svg>

<div class="abs sec-title" style="left:78px;top:672px"><span class="sec-mark"></span>Welcome To Summit Path Advisory</div>
<div class="abs dotted" style="left:78px;top:703px;width:472px"></div>
<div class="abs photo" style="left:79px;top:713px;width:95px;height:117px" role="img" aria-label="Portrait photo of the business coach"></div>
<p class="abs welcome-text">With over 25 years of experience in a variety of industries, we know the daily attitudes, habits and goals for successful companies begin with a plan.&nbsp; By training employees where needed and coaching to clear expectations writes success stories daily as the plan unfolds over the course of the year.<br>Together we’ll explore where YOU are and where YOU want to go. By building a solid vision as the leader, and communicating...</p>
<span class="abs read-more">Read More &gt;&gt;</span>
<div class="abs vdivider" style="left:571px;top:668px;height:185px"></div>

<div class="abs sec-title" style="left:593px;top:672px"><span class="sec-mark"></span>View Video</div>
<span class="abs arrows" style="left:786px;top:677px">‹›</span>
<div class="abs dotted" style="left:593px;top:703px;width:210px"></div>
<div class="abs side-video" role="img" aria-label="Video still of the coach presenting">
  <div class="video-bar"></div>
</div>

<div class="abs band"></div>

<div class="abs sec-title" style="left:78px;top:900px"><span class="sec-mark"></span>Client Testimonials</div>
<span class="abs arrows blue" style="left:530px;top:905px">‹ ›</span>
<div class="abs dotted" style="left:78px;top:931px;width:472px"></div>
<p class="abs quote"><span class="qmark">“</span> Dana is one of those unique sales trainers that not only brings her exceptional presentation skills and charisma to the classroom, but she also draws from her years of practical experience in getting and closing the sale.... READ MORE+ <span class="qmark">”</span></p>
<span class="abs quote-name">Marla Fenwick - Former Advanced Sales Training Manager</span>
<div class="abs quote-photo" role="img" aria-label="Photo of the client giving the testimonial"></div>
<div class="abs vdivider" style="left:571px;top:896px;height:140px"></div>

<div class="abs sec-title" style="left:593px;top:900px"><span class="sec-mark"></span>Our Members</div>
<div class="abs dotted" style="left:593px;top:931px;width:210px"></div>
<div class="abs members">
  <span class="badge"></span><span class="badge sq"></span><span class="badge gold"></span>
</div>

<footer>
  <div class="abs footer"></div>
  <div class="abs foot-mark"></div>
  <div class="abs vdivider" style="left:160px;top:1066px;height:86px;border-color:#d2d2ce"></div>
  <p class="abs foot-links">Home <span>•</span> Passion <span>•</span> Who We Are <span>•</span> Speaker <span>•</span> Free Videos <span>•</span> Web TV Show <span>•</span> Testimonials <span>•</span> Oakridge Learning <span>•</span> Blog <span>•</span> Contact Us</p>
  <div class="abs" style="left:160px;top:1095px;width:642px;border-top:1px solid #d8d8d4"></div>
  <div class="abs share">Share with us
    <span class="soc" style="background:#3a5a98"></span>
    <span class="soc" style="background:#2aa3d8"></span>
    <span class="soc" style="background:#1f7fa8"></span>
  </div>
  <p class="abs subscribe">Subscribe to <b>NEWSLETTER</b></p>
  <div class="abs email">Email Address</div>
  <div class="abs submit">SUBMIT</div>
  <div class="abs bottom">
    <span class="abs" style="left:80px;top:12px">Copyright 2014 - Summitpathadvisory - All rights Reserved</span>
    <span class="abs" style="left:630px;top:10px">Terms &amp; Conditions &nbsp;|&nbsp; Privacy Policy</span>
  </div>
</footer>

</body>
</html>
```